Quiet Hollow Journals - Book Covers - Ebook, Paperback, Hardcover

Title would be:
Quiet Hollow Journals
Subtitle: 9 Simple Steps Including, Site Selection, Pollination and Fertilization, Pruning, Small Spaces, Pest Control, Tropical Fruit Trees, and Berries
Author: Marguerite Olundvale
I would like the designer to have a couple of beautiful pictures on the cover. Please make it unique.
This would be posted on Brindlo so please use specifications for book covers on Brindlo
Back Cover should read:
Quiet Hollow Journals
9 Simple Steps Including, Site Selection, Pollination and Fertilization, Pruning, Small Spaces, Pest Control, Tropical Fruit Trees, and Berries
Marguerite Olundvale
How to grow a thriving orchard and reap a bountiful harvest in less than a year – in both urban and non-urban settings
Fruit trees are fun to grow and will reward you with years of fresh, juicy homegrown produce.
However, the process can be excruciating, especially if you don’t know the best varieties to grow or how to control pests and diseases.
With a little planning and guidance, you will soon be biting into mellow fruits from trees in your backyard – including cherries, plums, pears, apples, and more.
All you need is to learn how to care for the trees, which you will find inside.
In Quiet Hollow Journals, you’ll discover:
● How to pick the right fruit tree varieties for your growing zone and needs to ensure the plants don’t die
● How to effectively plan and prepare the planting site to lay a good foundation for your incoming trees
● How to choose the right irrigation system for your orchard and keep your fruit trees nourished all year long
● Examples of fruit garden plans for different regions – including a guide to help you design your small backyard space
● How to plant fruits to ensure proper pollination, fertilization, and flourishing growth of your produce
● Different fruit tree propagation methods with step-by-step instructions to help you grow your trees without spending money on costly grafts
● When and how to harvest fruits to ensure you collect them at their best and prevent wasting your hard work
● How to boost fruit production, encourage growth, and protect your trees from dangerous diseases
● How to look after fruit trees during all seasons, practice organic farming, and control pests in your garden
And much more…
It’s time to grow your mini-orchard and bask in years of harvest and sweetness from your labor.
Discover how you can have a thriving orchard and a bountiful fruit harvest.
Updates
Hello all Designers,
Please include this on the back cover as I forgot to include it in my main project:
Back Cover to read:
Quiet Hollow Journals
Marguerite Olundvale
And much more…
Target Market(s)
People Who Love Gardening
Industry/Entity Type
Publishing
Requirements
Must have
- Title, Subtitle, Author Name, Beautiful Design, Eye Catching making you want to buy the book
Nice to have
- Large title, Easy to read subtitle intriguing pictures
Should not have
- Busy with too much stuff going on

```html
<!DOCTYPE html>
<html lang="en">
<head>
<meta charset="utf-8">
<title>Quiet Hollow Journals – Cover Spread</title>
<link href="https://fonts.googleapis.com/css2?family=Bebas+Neue&family=Oswald:wght@400;500;600&family=Open+Sans:ital,wght@0,400;0,600;1,600&display=swap" rel="stylesheet">
<style>
  :root {
    --page-bg: #ffffff;
    --cover-top: #27301d;
    --cover-mid: #3f3a24;
    --cover-bottom: #6e5437;
    --ink-light: #ffffff;
    --ink-soft: #ecebe4;
    --ink-dark: #2a2618;
    --orchard-green: #6f8a3a;
    --orchard-light: #c9d08a;
    --fruit-orange: #e07b28;
    --fruit-red: #c9472b;
    --crate-light: #c9ab80;
    --crate-wood: #a4815a;
    --crate-shadow: #6f5436;
  }
  * { margin: 0; padding: 0; box-sizing: border-box; }
  html, body { width: 785px; height: 1200px; overflow: hidden; background: var(--page-bg); }

  .spread {
    position: absolute; left: 0; top: 315px;
    width: 785px; height: 569px; overflow: hidden;
    background: linear-gradient(180deg, var(--cover-top) 0%, var(--cover-mid) 45%, var(--cover-bottom) 100%);
  }

  /* Back cover */
  .back-cover { position: absolute; left: 0; top: 0; width: 369px; height: 569px; }
  .back-title {
    position: absolute; top: 28px; left: 0; width: 369px; text-align: center;
    font-family: "Bebas Neue", sans-serif; font-weight: 400; font-size: 38px; line-height: 1;
    color: var(--ink-light); letter-spacing: 1px;
  }
  .back-title-sub {
    position: absolute; top: 64px; left: 0; width: 369px; text-align: center;
    font-family: "Oswald", sans-serif; font-weight: 500; font-size: 13px; color: var(--ink-light);
    letter-spacing: 9px; padding-left: 9px;
  }
  .back-subtitle {
    position: absolute; top: 84px; left: 40px; width: 290px; text-align: center;
    font-family: "Oswald", sans-serif; font-weight: 400; font-size: 7.4px; line-height: 11.5px;
    color: var(--ink-light); text-transform: uppercase;
  }
  .blurb {
    position: absolute; top: 117px; left: 41px; width: 288px;
    font-family: "Open Sans", sans-serif; font-size: 7.6px; line-height: 11.4px; color: var(--ink-soft);
  }
  .blurb p { margin-bottom: 8px; }
  .blurb em { font-weight: 600; }
  .discover-list { list-style: none; margin: -4px 0 2px 0; }
  .discover-list li { position: relative; padding-left: 27px; text-align: justify; }
  .discover-list li::before {
    content: ""; position: absolute; left: 10px; top: 3px;
    width: 7px; height: 7px; border-radius: 50%; background: var(--ink-light);
  }
  .more { padding-left: 27px; font-style: italic; font-weight: 600; margin-bottom: 2px; }
  .isbn-box {
    position: absolute; left: 206px; top: 502px; width: 122px; height: 49px;
    background: var(--ink-light); display: flex; align-items: center; justify-content: center;
    font-family: "Oswald", sans-serif; font-size: 15px; letter-spacing: 11px; padding-left: 11px;
    color: var(--ink-dark);
  }

  /* Spine */
  .spine { position: absolute; left: 372px; top: 0; width: 40px; height: 569px; }
  .spine-title, .spine-author {
    position: absolute; left: 50%; writing-mode: vertical-rl; transform: translateX(-50%);
    color: var(--ink-light); white-space: nowrap;
  }
  .spine-title { top: 154px; font-family: "Bebas Neue", sans-serif; font-size: 22px; letter-spacing: 0.5px; }
  .spine-author { top: 432px; font-family: "Oswald", sans-serif; font-weight: 500; font-size: 9px; letter-spacing: 0.5px; }

  /* Front cover */
  .front-cover { position: absolute; left: 410px; top: 0; width: 375px; height: 569px; }
  .orchard-photo {
    position: absolute; left: -20px; top: 0; width: 395px; height: 330px;
    background:
      radial-gradient(ellipse 55% 38% at 45% 30%, var(--orchard-light) 0%, transparent 70%),
      radial-gradient(circle at 95% 10%, var(--fruit-orange) 0%, transparent 16%),
      linear-gradient(180deg, transparent 0%, var(--orchard-green) 25%, var(--orchard-green) 65%, transparent 100%);
    opacity: 0.8;
  }
  .crate-photo {
    position: absolute; left: 55px; top: 88px; width: 300px; height: 200px;
    border-radius: 6px;
    background:
      radial-gradient(ellipse 50% 30% at 50% 14%, var(--fruit-red) 0%, var(--fruit-orange) 45%, transparent 80%),
      linear-gradient(180deg, transparent 0%, transparent 26%, var(--crate-light) 30%, var(--crate-wood) 75%, var(--crate-shadow) 100%);
  }
  .front-author {
    position: absolute; top: 22px; left: 0; width: 375px; text-align: center;
    font-family: "Oswald", sans-serif; font-weight: 500; font-size: 16px; letter-spacing: 3.5px;
    color: var(--ink-dark); text-transform: uppercase;
  }
  .crate-label {
    position: absolute; font-family: "Oswald", sans-serif; font-weight: 500; color: var(--ink-dark);
    text-transform: uppercase; white-space: nowrap; transform-origin: left center;
  }
  .crate-label.steps { left: 84px; top: 164px; font-size: 13px; letter-spacing: 1.2px; transform: rotate(2deg); }
  .crate-label.line-one { left: 80px; top: 198px; font-size: 8.6px; transform: rotate(3.5deg); }
  .crate-label.line-two { left: 72px; top: 226px; font-size: 8.6px; transform: rotate(5deg); }
  .front-title {
    position: absolute; top: 282px; left: 0; width: 375px; text-align: center;
    font-family: "Bebas Neue", sans-serif; font-weight: 400; color: var(--ink-light); line-height: 0.9;
  }
  .front-title .word-one { display: block; font-size: 122px; }
  .front-title .word-two { display: block; font-size: 104px; margin-top: 2px; }
  .front-title-sub {
    position: absolute; top: 506px; left: 0; width: 375px; text-align: center;
    font-family: "Oswald", sans-serif; font-weight: 500; font-size: 28px; letter-spacing: 16px;
    padding-left: 16px; color: var(--ink-light);
  }
</style>
</head>
<body>
  <main class="spread">
    <section class="back-cover">
      <h2 class="back-title">QUIET HOLLOW</h2>
      <div class="back-title-sub">JOURNALS</div>
      <p class="back-subtitle">9 simple steps including site selection, pollination and fertilization,<br>pruning, small spaces, pest control, tropical fruit trees, and berries</p>
      <div class="blurb">
        <p>How to grow a thriving orchard and reap a bountiful harvest in less than a year – in both urban and non-urban settings Fruit trees are fun to grow and will reward you with years of fresh, juicy homegrown produce.</p>
        <p>However, the process can be excruciating, especially if you don’t know the best varieties to grow or how to control pests and diseases. With a little planning and guidance, you will soon be biting into mellow fruits from trees in your backyard – including cherries, plums, pears, apples, and more.</p>
        <p>All you need is to learn how to care for the trees, which you will find inside. <em>In Quiet Hollow Journals, you’ll discover:</em></p>
        <ul class="discover-list">
          <li>How to pick the right fruit tree varieties for your growing zone and needs to ensure the plants don’t die</li>
          <li>How to effectively plan and prepare the planting site to lay a good foundation for your incoming trees</li>
          <li>How to choose the right irrigation system for your orchard and keep your fruit trees nourished all year long</li>
          <li>Examples of fruit garden plans for different regions – including a guide to help you design your small backyard space</li>
          <li>How to plant fruits to ensure proper pollination, fertilization, and flourishing growth of your produce</li>
          <li>Different fruit tree propagation methods with step-by-step instructions to help you grow your trees without spending money on costly grafts</li>
          <li>When and how to harvest fruits to ensure you collect them at their best and prevent wasting your hard work</li>
          <li>How to boost fruit production, encourage growth, and protect your trees from dangerous diseases</li>
          <li>How to look after fruit trees during all seasons, practice organic farming, and control pests in your garden.</li>
        </ul>
        <p class="more">And much more…</p>
        <p>It’s time to grow your mini-orchard and bask in years of harvest and sweetness from your labor. Discover how you can have a thriving orchard and a bountiful fruit harvest.</p>
      </div>
      <div class="isbn-box">ISBN</div>
    </section>

    <section class="spine">
      <div class="spine-title">QUIET HOLLOW JOURNALS</div>
      <div class="spine-author">MARGUERITE OLUNDVALE</div>
    </section>

    <section class="front-cover">
      <div class="orchard-photo" role="img" aria-label="Blurred sunlit orchard with green trees and hanging oranges"></div>
      <div class="crate-photo" role="img" aria-label="Photo of a rustic wooden crate piled with oranges and colourful fruit, resting on a wooden table"></div>
      <div class="front-author">Marguerite Olundvale</div>
      <div class="crate-label steps">9 simple steps including</div>
      <div class="crate-label line-one">Site selection, pollination and fertilization, pruning,</div>
      <div class="crate-label line-two">Small spaces, pest control, tropical fruit trees, and berries</div>
      <h1 class="front-title"><span class="word-one">QUIET</span><span class="word-two">HOLLOW</span></h1>
      <div class="front-title-sub">JOURNALS</div>
    </section>
  </main>
</body>
</html>
```